THE SHRIEKING AT BRAMBLEMOOR Prospectus/Deck

We need a prospectus/deck made for this Halloween event called THE SHRIEKING AT BRAMBLEMOOR. Attached is the writeup, our logo, some background photos you can use, and photos of the actual town site. For the town photos (4) could you try to make them look greyscale or smokey? I attached a sample Prospectus/Deck that was created for another event of ours to give you an idea of layout and pages.

```html
<!DOCTYPE html>
<html lang="en">
<head>
<meta charset="utf-8">
<title>The Shrieking at Bramblemoor – Prospectus</title>
<link href="https://fonts.googleapis.com/css2?family=Creepster&family=Oswald:wght@400;500&family=Poppins:wght@400;500;600;700;800&display=swap" rel="stylesheet">
<style>
:root{
  --sheet:#ffffff;
  --ink:#ffffff;
  --slime:#8fae3a;
  --slime-dark:#5f7d22;
  --amber:#f5b935;
  --night:#120e0b;
  --band-text:#1a1409;
}
*{box-sizing:border-box;margin:0;padding:0}
html,body{width:993px;height:1200px;overflow:hidden;background:var(--sheet)}
body{position:relative;font-family:"Poppins",sans-serif;color:var(--ink)}
.page{position:absolute;width:413px;height:319px;overflow:hidden;background:var(--night);box-shadow:4px 6px 10px rgba(0,0,0,.45)}
.col-l{left:64px}.col-r{left:506px}
.row-1{top:82px}.row-2{top:436px}.row-3{top:789px}
.photo{position:absolute;inset:0}
.abs{position:absolute}
.scare{font-family:"Creepster",sans-serif;color:var(--slime);letter-spacing:.5px;line-height:1;font-weight:400}
.eyebrow{font-size:5px;letter-spacing:2px;color:var(--amber);font-weight:500}
.brand{font-family:"Poppins",sans-serif;font-weight:800;color:var(--slime);font-size:13px;letter-spacing:.2px;line-height:1}
.body{font-size:6.3px;line-height:8.1px;color:#f1ece4}
.web-band{position:absolute;left:0;bottom:26px;height:17px;background:var(--amber);clip-path:polygon(0 0,92% 5%,100% 55%,91% 100%,0 100%);display:flex;align-items:center;padding-left:27px;font-size:8px;letter-spacing:.6px;color:var(--band-text)}
.web-band b{font-weight:700}
.pg{position:absolute;right:24px;bottom:30px;font-size:7px;font-weight:700;color:var(--amber)}
.dates{display:flex;align-items:center;gap:5px}
.dates .month{font-family:"Creepster",sans-serif;color:#fff;font-size:15px;line-height:1}
.dates .range{font-family:"Creepster",sans-serif;color:var(--amber);font-size:27px;line-height:1}
.dates .year{border:1px solid var(--amber);writing-mode:vertical-rl;font-size:7px;letter-spacing:1.5px;padding:2px 1px;color:#fff}
.dates .count{font-family:"Oswald",sans-serif;line-height:.95}
.dates .count .n{font-size:22px;color:#fff;display:block}
.dates .count .d{font-size:19px;color:var(--amber);display:block}
.address{display:flex;align-items:center;gap:3px;font-size:8px;font-weight:500}
.bullets{list-style:none;font-size:5px;line-height:6px}
.bullets li{position:relative;padding-left:7px;margin-bottom:4px}
.bullets li::before{content:"";position:absolute;left:0;top:1.3px;width:3.4px;height:3.4px;border-radius:50%;background:var(--slime)}
.tier-tag{position:absolute;height:11px;width:104px;font-size:5px;font-weight:700;display:flex;align-items:center;justify-content:center;color:#222;clip-path:polygon(4% 0,100% 0,94% 100%,0 100%)}
.tier-price{position:absolute;font-size:11px;font-weight:700;color:var(--amber)}
.tier-list{position:absolute;width:90px;font-size:3.8px;line-height:4.6px}
.tier-list li{margin-bottom:3.4px}
.tier-list li::before{top:.6px;width:3px;height:3px}
.icon{position:absolute;width:30px;height:30px}
</style>
</head>
<body>

<!-- Cover -->
<section class="page col-l row-1">
  <div class="photo" role="img" aria-label="Masked forest creature in a dark robe standing among autumn trees" style="background:linear-gradient(90deg,#17110c 0%,#2a1c13 45%,#4a3020 70%,#2b1d14 100%)"></div>
  <p class="abs eyebrow" style="left:46px;top:28px">THE SHRIEKING AT</p>
  <p class="abs brand" style="left:27px;top:38px;font-size:17px">BRAMBLEMOOR</p>
  <h1 class="abs scare" style="left:27px;top:88px;font-size:33px">HALLOWEEN</h1>
  <p class="abs" style="left:27px;top:122px;font-size:36px;letter-spacing:15px;font-weight:400;line-height:1">EVENT</p>
  <div class="abs dates" style="left:27px;top:182px">
    <div><div class="month">OCTOBER</div><div class="range">6 - 31</div></div>
    <div class="year">2023</div>
    <div class="count"><span class="n">17</span><span class="d">DAYS</span></div>
  </div>
  <p class="abs address" style="left:27px;top:236px">
    <svg width="7" height="9" viewBox="0 0 10 14"><path d="M5 0a5 5 0 0 1 5 5c0 4-5 9-5 9S0 9 0 5a5 5 0 0 1 5-5z" fill="#8fae3a"/><circle cx="5" cy="5" r="2" fill="#17110c"/></svg>
    1450 Concession Road 9, Millbrook Ridge, Ontario K0L 2P0
  </p>
  <div class="web-band" style="width:265px;font-size:10px">www.<b>shriekingatbramblemoor</b>.ca</div>
</section>

<!-- Introduction -->
<section class="page col-r row-1">
  <div class="photo" role="img" aria-label="Hooded reaper with a scythe in blue-green fog" style="background:linear-gradient(100deg,#0f2a2a 0%,#1d4545 40%,#2f5d62 65%,#142a30 100%)"></div>
  <h2 class="abs scare" style="left:27px;top:32px;font-size:28px">INTRODUCTION</h2>
  <div class="abs body" style="left:27px;top:70px;width:203px">
    <p>Welcome to The Shrieking at Bramblemoor, where terror meets Hollywood magic! Step into our nightmare-inducing event set within a sprawling film studio lot at 1450 Concession Road 9, Millbrook Ridge, Ontario K0L 2P0 which has been transformed into a chillingly realistic little town. As you enter, you will find yourself immersed in the eerie atmosphere of a bygone era, where each corner holds lurking horrors. Our haunted experience offers a unique opportunity for vendors to become part of the terror by occupying the shops that line the Main Street of this sinister town. From creepy curiosities to spine-chilling treats, your store front will become a focal point of fear, allowing visitors to not only scream but also shop amidst the horrors. Prepare for a spinetingling journey like no other as you explore our haunted event in this hauntingly realistic town.</p>
    <p style="margin-top:8px">The Shrieking at Bramblemoor is an an exhilarating and spine-chilling haunted town experience that promises to deliver unforgettable thrills and scares. As we gear up for another terrifying season, we invite you to join us as a valued vendor or sponsor. This prospectus outlines the various opportunities available for your brand to be part of this highly anticipated event.</p>
  </div>
  <div class="web-band" style="width:190px">www.<b>shriekingatbramblemoor</b>.ca</div>
  <span class="pg">Pg 1</span>
</section>

<!-- About -->
<section class="page col-l row-2">
  <div class="photo" role="img" aria-label="Ghostly figure in tattered white robes with branch antlers in misty overgrown field" style="background:linear-gradient(90deg,#0e0d0b 0%,#121210 38%,#4d5246 62%,#6f7668 80%,#3e4637 100%)"></div>
  <h2 class="abs scare" style="left:27px;top:27px;font-size:19px;line-height:1.05">ABOUT THE SHRIEKING<br>AT BRAMBLEMOOR</h2>
  <p class="abs body" style="left:27px;top:78px;width:205px"><span style="color:var(--amber);font-weight:500">The Shrieking at Bramblemoor</span> is a premier haunted town attraction known for its immersive and interactive experience that pushes the boundaries of fear. Our haunted town offers a meticulously designed setting with elaborate sets, talented actors, and cutting-edge special effects to create an atmosphere of horror and suspense. We attract a diverse audience of thrill-seekers, horror enthusiasts, families, and groups of friends, ensuring a wide reach for your brand.</p>
  <p class="abs" style="left:27px;top:172px;font-size:8px;letter-spacing:2.5px">EVENT DETAILS</p>
  <div class="abs dates" style="left:27px;top:192px">
    <div><div class="month" style="font-size:13px">OCTOBER</div><div class="range" style="font-size:23px">6 - 31</div></div>
    <div class="year" style="font-size:6px">2023</div>
    <div class="count"><span class="n" style="font-size:19px">17</span><span class="d" style="font-size:17px">DAYS</span></div>
  </div>
  <p class="abs address" style="left:27px;top:235px;font-size:7px">
    <svg width="6" height="8" viewBox="0 0 10 14"><path d="M5 0a5 5 0 0 1 5 5c0 4-5 9-5 9S0 9 0 5a5 5 0 0 1 5-5z" fill="#8fae3a"/><circle cx="5" cy="5" r="2" fill="#0e0d0b"/></svg>
    1450 Concession Road 9, Millbrook Ridge, Ontario K0L 2P0
  </p>
  <div class="web-band" style="width:190px">www.<b>shriekingatbramblemoor</b>.ca</div>
  <span class="pg">Pg 2</span>
</section>

<!-- Vendors -->
<section class="page col-r row-2">
  <div class="photo" role="img" aria-label="Bloodied man in overalls leaning over a workbench in a rundown shed" style="background:linear-gradient(90deg,#141210 0%,#1f1c18 40%,#4a4236 65%,#5e564a 85%,#3a342c 100%)"></div>
  <h2 class="abs scare" style="left:27px;top:27px;font-size:19px">VENDOR OPPORTUNITIES</h2>
  <h3 class="abs" style="left:27px;top:57px;font-size:12px;font-weight:600">ON-SITE VENDORS</h3>
  <p class="abs" style="left:27px;top:72px;font-size:6.5px">Starting at <b style="color:var(--amber);font-size:10px">$2500 + HST</b> (per vendor; no sharing)</p>
  <p class="abs" style="left:27px;top:84px;width:200px;font-size:6.5px;line-height:7.5px;color:var(--slime)">depending on location and type of products/services sold and offered</p>
  <p class="abs body" style="left:27px;top:107px;width:200px;font-size:6.6px">Set up your booth within the haunted town premises and showcase your products or services to a captive audience in one of the existing buildings. Your brand will be exposed to thousands of visitors throughout the event. Examples of suitable vendors include</p>
  <ul class="abs bullets" style="left:27px;top:157px;width:110px">
    <li>Halloween costume shops</li>
    <li>Horror-themed merchandise</li>
    <li>Local/Artisan food vendors (pre-packaged items)</li>
    <li>Face painting and special effects makeup artists</li>
  </ul>
  <ul class="abs bullets" style="left:143px;top:157px;width:90px">
    <li>Paranormal investigators or ghost tour guides</li>
    <li>Novelty and souvenir vendors</li>
    <li>Psychic</li>
    <li>Metaphysical items and crystals</li>
  </ul>
  <p class="abs" style="left:27px;top:226px;font-size:11px;font-weight:700;line-height:11px">FOOD<br>TRUCKS</p>
  <div class="abs" style="left:84px;top:225px;height:22px;border-left:1px solid #bbb"></div>
  <p class="abs" style="left:91px;top:225px;font-size:8.5px;line-height:10px"><b style="color:var(--amber);font-size:10px">$5000 + HST</b><br>max of 3-4 total</p>
  <div class="web-band" style="width:190px">www.<b>shriekingatbramblemoor</b>.ca</div>
  <span class="pg">Pg 3</span>
</section>

<!-- Promotions -->
<section class="page col-l row-3">
  <div class="photo" role="img" aria-label="Stormy sky over a cornfield with weathered wooden crosses and a crow" style="background:linear-gradient(180deg,#4a5244 0%,#353d33 40%,#232a20 70%,#181d15 100%)"></div>
  <p class="abs eyebrow" style="left:44px;top:21px">THE SHRIEKING AT</p>
  <p class="abs brand" style="left:29px;top:30px;font-size:15px">BRAMBLEMOOR</p>
  <svg class="icon" style="left:28px;top:80px" viewBox="0 0 30 30" fill="none" stroke="#f5b935" stroke-width="1.8" stroke-linejoin="round">
    <path d="M4 15l14-8v16L4 18z"/><path d="M6 18l3 8h3l-2-7"/><path d="M22 10l4-3M23 15h5M22 20l4 3"/>
  </svg>
  <h3 class="abs scare" style="left:78px;top:83px;font-size:12px">PROMOTIONAL GIVEAWAYS</h3>
  <p class="abs body" style="left:78px;top:97px;width:172px;font-size:6.8px;line-height:8.2px">Partner with us to provide branded merchandise or samples to be distributed to our visitors. This opportunity allows you to directly engage with attendees and create lasting impressions of your brand.</p>
  <svg class="icon" style="left:28px;top:162px" viewBox="0 0 30 30" fill="none" stroke="#f5b935" stroke-width="1.6" stroke-linejoin="round">
    <path d="M2 10l6-3 6 4 6-4 7 3"/><path d="M2 10v8l9 8 3-2 3 2 9-8v-8"/><path d="M14 11l-4 4 3 2 4-3"/>
  </svg>
  <h3 class="abs scare" style="left:78px;top:167px;font-size:12px">EXCLUSIVE SPONSORSHIP</h3>
  <p class="abs body" style="left:78px;top:181px;width:182px;font-size:6.8px;line-height:8.2px">Become an exclusive sponsor of The Shrieking at Bramblemoor. This comprehensive package offers maximum exposure and recognition for your brand. Benefits may include prominent logo placement, branding on event merchandise, onsite signage, social media promotions, and more. This option is ideal for businesses looking to establish a strong association with the haunted town and its audience.</p>
  <div class="web-band" style="width:190px">www.<b>shriekingatbramblemoor</b>.ca</div>
  <span class="pg">Pg 4</span>
</section>

<!-- Sponsorship -->
<section class="page col-r row-3">
  <div class="photo" role="img" aria-label="Burning forest with orange glow and dark silhouetted trees" style="background:linear-gradient(100deg,#1a120d 0%,#2b1b12 40%,#5a2e14 65%,#3a2216 85%,#1d1410 100%)"></div>
  <h2 class="abs scare" style="left:27px;top:33px;font-size:17px">SPONSORSHIP TIERS</h2>
  <p class="abs body" style="left:27px;top:55px;width:218px;font-size:6.8px;line-height:8.1px">We offer different sponsorship tiers to suit your marketing goals and budget. Please note that availability is limited for each tier, and commitments will be honored on a firstcome, first-served basis. The sponsorship tiers include:</p>
  <p class="abs eyebrow" style="left:303px;top:27px">THE SHRIEKING AT</p>
  <p class="abs brand" style="left:286px;top:36px;font-size:15px">BRAMBLEMOOR</p>

  <div class="tier-tag" style="left:24px;top:106px;background:#d8d8d8">PLATINUM SPONSORSHIP</div>
  <div class="tier-tag" style="left:135px;top:106px;background:var(--amber)">GOLD SPONSORSHIP</div>
  <div class="tier-tag" style="left:249px;top:106px;background:#e6e6e6">SILVER SPONSORSHIP</div>
  <p class="tier-price" style="left:36px;top:120px">$15,000 + HST</p>
  <p class="tier-price" style="left:146px;top:120px">$10,000 + HST</p>
  <p class="tier-price" style="left:261px;top:120px">$5,000 + HST</p>
  <ul class="bullets tier-list" style="left:30px;top:138px">
    <li>Prominent logo placement on all marketing materials, including website, posters, flyers, and social media promotions</li>
    <li>Exclusive branding on event merchandise</li>
    <li>On-site signage and banners featuring your brand</li>
    <li>Dedicated social media posts highlighting your sponsorship</li>
    <li>Recognition during event announcements and media interviews</li>
    <li>Complimentary tickets for your staff or clients</li>
  </ul>
  <ul class="bullets tier-list" style="left:140px;top:138px">
    <li>Logo placement on select marketing materials, including website, posters, and social media promotions</li>
    <li>On-site signage featuring your brand</li>
    <li>Social media mentions acknowledging your sponsorship</li>
    <li>Complimentary tickets for your staff or clients</li>
  </ul>
  <ul class="bullets tier-list" style="left:255px;top:138px">
    <li>Logo placement on event website and select marketing materials</li>
    <li>On-site signage featuring your brand</li>
    <li>Complimentary tickets for your staff or clients</li>
  </ul>
  <p class="abs" style="left:27px;top:235px;width:310px;font-size:4.3px;line-height:5.4px">We are open to customizing sponsorship packages to meet your specific needs and objectives.<br>If you are interested in becoming a vendor or sponsor for The Shrieking at Bramblemoor, please contact us at the following:</p>
  <p class="abs" style="left:27px;top:247px;font-size:8px;font-weight:700;color:var(--amber)">marnie@nightfallevents.ca</p>
  <p class="abs" style="left:27px;top:259px;width:315px;font-size:4.3px;line-height:5.4px">We would be delighted to discuss the available opportunities in more detail and tailor a package that aligns with your brand's goals. Do not miss the chance to be part of a frightfully fantastic experience that will haunt your customers' memories for years to come. Join The Shrieking at Bramblemoor as a vendor or sponsor and make this haunted town season one to remember!</p>
  <div class="web-band" style="width:190px">www.<b>shriekingatbramblemoor</b>.ca</div>
  <span class="pg">Pg 5</span>
</section>

</body>
</html>
```